Business card for STEADYLINE

Please design professional business card for IT consulting firm STEADYLINE INC.
Use logo attached.
Use information from sample tRove business card attached.
replace trove inc with STEADYLINE INC.
as well as troveinc.com with steadyline.example

```html
<!DOCTYPE html>
<html lang="en">
<head>
<meta charset="utf-8">
<title>STEADYLINE business card</title>
<link rel="stylesheet" href="https://fonts.googleapis.com/css2?family=Arimo:wght@400;700&display=swap">
<style>
  :root {
    --page: #e9e9e9;
    --card: #2e2e2f;
    --card-back: #323233;
    --ink: #ffffff;
    --accent: #f28c1e;
    --teal: #46f5d4;
    --sky: #3fd6f7;
    --violet: #9414e0;
    --pink: #d54a8a;
    --emboss: #262627;
  }
  * { box-sizing: border-box; margin: 0; padding: 0; }
  html, body { width: 1200px; height: 802px; overflow: hidden; }
  body {
    background: var(--page);
    font-family: "Arimo", Arial, sans-serif;
    display: flex;
    align-items: center;
    justify-content: center;
    gap: 48px;
  }
  .card {
    width: 525px;
    height: 300px;
    border-radius: 3px;
    position: relative;
    overflow: hidden;
    box-shadow: 0 6px 18px rgba(0,0,0,0.18);
  }
  .card--front { background: var(--card); }
  .card--back {
    background: var(--card-back);
    display: flex;
    align-items: center;
    justify-content: center;
  }
  .details {
    position: absolute;
    left: 34px;
    top: 34px;
    width: 280px;
    color: var(--ink);
  }
  .person-name {
    color: var(--accent);
    font-weight: 700;
    font-size: 16px;
    letter-spacing: 0.2px;
  }
  .person-role { font-size: 14px; margin-top: 3px; letter-spacing: 0.3px; }
  .contact-list { list-style: none; margin-top: 20px; }
  .contact-list li {
    display: flex;
    align-items: center;
    gap: 9px;
    font-size: 14px;
    line-height: 21px;
    white-space: nowrap;
  }
  .contact-icon { width: 13px; height: 13px; flex: none; }
  .company-name {
    color: var(--accent);
    font-weight: 700;
    font-size: 15px;
    margin-top: 22px;
  }
  .company-address { font-size: 14px; line-height: 19px; margin-top: 2px; white-space: nowrap; }
  .brand-zone {
    position: absolute;
    right: 0;
    top: 0;
    width: 195px;
    height: 100%;
  }
  .colour-block {
    position: absolute;
    left: 0;
    right: 0;
    height: 112px;
  }
  .colour-block--top {
    top: 0;
    background: linear-gradient(180deg, var(--teal) 0%, var(--sky) 45%, var(--violet) 100%);
  }
  .colour-block--bottom {
    bottom: 0;
    background: linear-gradient(180deg, var(--pink) 0%, var(--accent) 60%);
  }
  .wordmark {
    display: flex;
    align-items: center;
    gap: 7px;
    color: var(--ink);
    font-weight: 700;
    font-size: 22px;
    letter-spacing: 2px;
  }
  .brand-zone .wordmark {
    position: absolute;
    left: 0;
    right: 0;
    top: 112px;
    height: 76px;
    justify-content: center;
  }
  .wordmark-square { width: 9px; height: 9px; background: var(--ink); }
  .wordmark--embossed {
    color: var(--emboss);
    font-size: 46px;
    letter-spacing: 5px;
  }
</style>
</head>
<body>
  <section class="card card--front" aria-label="Card front">
    <div class="details">
      <p class="person-name">DANIEL VORONOV, P. ENG.</p>
      <p class="person-role">GENERAL MANAGER</p>
      <ul class="contact-list">
        <li>
          <svg class="contact-icon" viewBox="0 0 16 16" aria-hidden="true"><path fill="var(--accent)" d="M3 1l3 3-2 2c1 2 3 4 5 5l2-2 3 3-2 3C7 15 1 9 1 3z"/></svg>
          (555) 014-2270 ext.201
        </li>
        <li>
          <svg class="contact-icon" viewBox="0 0 16 16" aria-hidden="true"><rect x="4" y="1" width="8" height="14" rx="1.5" fill="none" stroke="var(--accent)" stroke-width="1.8"/></svg>
          (555) 019-3048
        </li>
        <li>
          <svg class="contact-icon" viewBox="0 0 16 16" aria-hidden="true"><rect x="1" y="3" width="14" height="10" fill="var(--accent)"/><path d="M1 3l7 6 7-6" fill="none" stroke="var(--card)" stroke-width="1.4"/></svg>
          dvoronov@steadyline.example
        </li>
        <li>
          <svg class="contact-icon" viewBox="0 0 16 16" aria-hidden="true"><circle cx="8" cy="8" r="6.5" fill="none" stroke="var(--accent)" stroke-width="1.8"/><path d="M1.5 8h13M8 1.5c-3 3-3 10 0 13M8 1.5c3 3 3 10 0 13" fill="none" stroke="var(--accent)" stroke-width="1.2"/></svg>
          www.steadyline.example
        </li>
      </ul>
      <p class="company-name">STEADYLINE INC.</p>
      <p class="company-address">120 Harbour Ln., Suite 204<br>Northbridge, Ontario, A1B 2C3, Canada</p>
    </div>
    <div class="brand-zone">
      <div class="colour-block colour-block--top" role="img" aria-label="Decorative colour block in teal, blue and violet"></div>
      <div class="wordmark"><span>STEADYLINE</span><span class="wordmark-square"></span></div>
      <div class="colour-block colour-block--bottom" role="img" aria-label="Decorative colour block in pink and orange"></div>
    </div>
  </section>

  <section class="card card--back" aria-label="Card back">
    <div class="wordmark wordmark--embossed"><span>STEADYLINE</span></div>
  </section>
</body>
</html>
```